Redesign of my Homepage - Online resource for anyone to learn American Sign Language

I would like to have a new homepage design http://www.HandwiseLessons.example . My business is a website for anyone to learn American Sign Language. There are over 300 video lessons, with each lesson having 20 vocabulary words, retention exercises, 16,000 video dictionary etc. It is a very extensive site. It is a self paced website. If you need a log in to see what customers see, please let me know. I would like to keep the same color scheme. I want the website to look modern and clean. I want a fresh look! I want something that is easy to navigate, attracts customers, and easy to follow. I would like the final design to communicate that my website is for anyone to learn how to sign with this incredible program.

Target Market(s)

Students taking American Sign Language, Parents with Deaf children, future interpreters for the deaf, co-workers of the Deaf. Also, schools that offer American Sign Language (online schools, homeschools, etc. ).

Industry/Entity Type

Business

Number of Pages Required

1 page

Requirements
Must have
• My project must be very clean and clear. I want my homepage to show that this is a program for people to learn how American Sign Language.
Nice to have
• Not sure. Surprise me.

```html
<!DOCTYPE html>
<html lang="en">
<head>
<meta charset="utf-8">
<title>Handwise Lessons – Learn ASL Online</title>
<link href="https://fonts.googleapis.com/css2?family=Open+Sans:wght@300;400;600;700&family=Arimo:wght@400&display=swap" rel="stylesheet">
<style>
  :root{
    --green:#0ca84a;
    --green-deep:#03982f;
    --green-mid:#049a3a;
    --btn:#078c35;
    --btn-edge:#3fc06e;
    --white:#ffffff;
    --ink-soft:#8d8d8d;
    --footer-bg:#d9dbdb;
    --footer-ink:#555a5a;
  }
  *{box-sizing:border-box;margin:0;padding:0}
  html,body{width:1124px;height:1200px;overflow:hidden;background:var(--white)}
  body{font-family:"Open Sans",sans-serif;color:var(--white)}

  .site-header{height:96px;position:relative}
  .brand{position:absolute;left:108px;top:26px;display:flex;align-items:center;gap:8px}
  .brand-mark{width:22px;height:22px;background:var(--green)}
  .brand-name{font-family:"Open Sans",sans-serif;font-weight:600;font-size:32px;color:var(--green);letter-spacing:-0.5px}
  .utility{position:absolute;right:128px;top:56px;display:flex;align-items:center;gap:18px;color:var(--ink-soft);font-size:13px}
  .login{display:flex;align-items:center;gap:5px;margin-right:18px}
  .social-dot{width:14px;height:14px;background:#a9a9a9;border-radius:3px}
  .search{margin-left:26px}

  .main-nav{height:58px;background:var(--green);display:flex;align-items:stretch;padding-left:104px}
  .nav-item{display:flex;align-items:center;gap:4px;padding:0 10px;font-size:11.5px;font-weight:700;color:var(--white);text-transform:uppercase;letter-spacing:-0.1px}
  .nav-item.active{background:var(--green-deep);padding:0 16px;margin-right:8px;margin-top:-2px;height:60px}
  .nav-item svg{width:10px;height:10px;fill:var(--white)}
  .caret{font-size:8px;margin-left:2px}

  .hero{height:416px;position:relative;background:linear-gradient(100deg,#8f8a80 0%,#a87f62 30%,#b8423f 48%,#6d6a5f 70%,#5a5b52 100%)}
  .hero-copy{position:absolute;left:686px;top:134px;width:340px}
  .hero-title{font-size:38px;font-weight:700;line-height:1.1;letter-spacing:-0.3px}
  .hero-text{font-size:18.5px;font-weight:400;line-height:26px;margin-top:6px}
  .btn{display:inline-block;background:var(--btn);border:1px solid var(--btn-edge);border-radius:18px;color:var(--white);font-weight:700;font-size:14px;text-transform:uppercase;padding:8px 18px}
  .hero .btn{margin:22px 0 0 108px}

  .audiences{display:flex;height:390px}
  .audience{flex:1;background:var(--green);padding:44px 0 0 54px;position:relative}
  .audience.featured{background:var(--green-mid)}
  .audience h2{font-size:26px;font-weight:700;line-height:35px;height:78px;width:290px}
  .audience .photo{width:268px;height:104px;margin-top:12px;margin-left:-10px}
  .audience p{font-family:"Arimo",sans-serif;font-size:17px;line-height:23px;margin-top:14px;margin-left:-4px;width:280px}
  .audience .btn{position:absolute;left:118px;top:305px}

  .site-footer{height:240px;background:var(--footer-bg);color:var(--footer-ink);text-align:center;font-size:12.5px;font-weight:400;padding-top:46px}
  .about{line-height:18px}
  .footer-links{margin-top:20px}
  .legal{margin-top:10px}
</style>
</head>
<body>
  <header class="site-header">
    <div class="brand"><span class="brand-mark"></span><span class="brand-name">handwise</span></div>
    <div class="utility">
      <span class="login">
        <svg width="12" height="12" viewBox="0 0 12 12"><circle cx="6" cy="3.5" r="3" fill="#a9a9a9"/><path d="M0 12c0-4 3-5 6-5s6 1 6 5z" fill="#a9a9a9"/></svg>
        Login/Register
      </span>
      <span class="social-dot"></span>
      <span class="social-dot"></span>
      <span class="social-dot"></span>
      <span class="social-dot"></span>
      <svg class="search" width="12" height="12" viewBox="0 0 12 12"><circle cx="5" cy="5" r="3.8" fill="none" stroke="#a9a9a9" stroke-width="1.6"/><path d="M8 8l3 3" stroke="#a9a9a9" stroke-width="1.8"/></svg>
    </div>
  </header>

  <nav class="main-nav">
    <span class="nav-item active"><svg viewBox="0 0 10 10"><path d="M5 0l5 5H8.5v5H6V7H4v3H1.5V5H0z"/></svg>Home</span>
    <span class="nav-item"><svg viewBox="0 0 10 10"><circle cx="5" cy="5" r="3.5" fill="none" stroke="#fff" stroke-width="1.8"/></svg>How it works<span class="caret">▼</span></span>
    <span class="nav-item"><svg viewBox="0 0 10 10"><path d="M0 1h10v8H0z M1.5 3v1h7V3z M1.5 5.5v1h7v-1z" fill-rule="evenodd"/></svg>Gift Certificates</span>
    <span class="nav-item"><svg viewBox="0 0 10 10"><path d="M4 0h2v4h2L5 7 2 4h2z M0 8h10v2H0z"/></svg>Try it free</span>
    <span class="nav-item"><svg viewBox="0 0 10 10"><path d="M0 1h2l1 5h6l1-4H3" /><circle cx="4" cy="8.5" r="1"/><circle cx="8" cy="8.5" r="1"/></svg>Buy now</span>
    <span class="nav-item"><svg viewBox="0 0 10 10"><path d="M0 2h10v6H0z"/></svg>Contact us<span class="caret">▼</span></span>
    <span class="nav-item"><svg viewBox="0 0 10 10"><circle cx="3.5" cy="3" r="2"/><circle cx="7" cy="3.5" r="1.6"/><path d="M0 9c0-3 2-4 3.5-4S7 6 7 9z"/></svg>Group rate form</span>
    <span class="nav-item">? Teacher's Guide</span>
  </nav>

  <section class="hero" role="img" aria-label="Photo of a mother signing to her young son outdoors, with another child behind them">
    <div class="hero-copy">
      <h1 class="hero-title">Lean ASL online</h1>
      <p class="hero-text">Duis sed odio sit amet nibh vulputate cursus a sit amet mauris.</p>
      <span class="btn">Try it free</span>
    </div>
  </section>

  <section class="audiences">
    <article class="audience">
      <h2>Learning Community</h2>
      <div class="photo" role="img" aria-label="Photo of a girl signing in a classroom" style="background:linear-gradient(90deg,#5a3f33,#b99a7c 50%,#c9a15a)"></div>
      <p>Anyone that has a passion to learn American Sign Language (ASL)</p>
      <span class="btn">+ Learn more</span>
    </article>
    <article class="audience featured">
      <h2>Hearing parents of deaf children</h2>
      <div class="photo" role="img" aria-label="Photo of a parent and child practising signs together" style="background:linear-gradient(90deg,#7c8a93,#c9b2a4 50%,#6e5a58)"></div>
      <p>Learn to communicate more effectively with your child</p>
      <span class="btn">+ Learn more</span>
    </article>
    <article class="audience">
      <h2>Deaf and hard of hearing</h2>
      <div class="photo" role="img" aria-label="Photo of a teacher and young student signing in a classroom" style="background:linear-gradient(90deg,#3a2b26,#c7b9b0 50%,#2f4b3a)"></div>
      <p>Learn to tackle the challenges you faced in the classroom</p>
      <span class="btn">+ Learn more</span>
    </article>
  </section>

  <footer class="site-footer">
    <p class="about">Handwise Lessons is a subscription based website for American Sign Language (ASL). The content is for anyone who wishes<br>to learn ASL, regardless of age. It has been designed to instruct deaf students, parents of deaf children, and the community-at-large.<br>You may cancel your subscription at any time. All lessons are taught by Deaf experts of ASL.</p>
    <p class="footer-links">Contact Us | Our Mission | Terms &amp; Conditions</p>
    <p class="legal">HandwiseLessons ©2017 All Rights Reserved | 1485286365.6586s</p>
  </footer>
</body>
</html>
```